quorvaAgency Business Card Design Project

We need a business card design for quorvaAgency. quorvaAgency is an underwriting agency. Underwriting agencies act on behalf of insurers, to underwrite insurance. We will be operating in specialised classes of insurance initially and looking to expand from there. We would like to see designs that incorporate our logo colours as well as a contrasting stand out colour - also we'd like the logo itself to be embossed on the card.

Industry/Entity Type

Insurance

Requirements
Must have
• Logo on front
Nice to have
• Logo solely featured on back of card
Should not have
• Please do not use comic cans font :)

```html
<!DOCTYPE html>
<html lang="en">
<head>
<meta charset="utf-8">
<title>quorvaAgency Business Cards</title>
<link rel="stylesheet" href="https://fonts.googleapis.com/css2?family=Open+Sans:wght@400;600&family=Tinos:wght@700&display=swap">
<style>
  :root {
    --page: #ffffff;
    --navy-deep: #061a4a;
    --navy: #0b2a6e;
    --navy-mid: #17428f;
    --glow: #3f78c4;
    --mark-line: #8cc2ff;
    --panel: rgba(120, 160, 220, 0.22);
    --band: #03123a;
    --rule: rgba(160, 195, 240, 0.45);
    --text-light: #ffffff;
    --text-soft: #dbe6f7;
  }
  * { box-sizing: border-box; margin: 0; padding: 0; }
  html, body {
    width: 1200px;
    height: 801px;
    overflow: hidden;
    background: var(--page);
  }
  .canvas {
    position: relative;
    width: 1200px;
    height: 801px;
  }
  .card {
    position: absolute;
    border-radius: 34px;
    overflow: hidden;
    box-shadow: 0 14px 22px rgba(0, 0, 0, 0.45);
  }
  .card-bokeh {
    position: absolute;
    inset: 0;
    background:
      radial-gradient(ellipse at 30% 30%, var(--glow) 0%, transparent 55%),
      radial-gradient(ellipse at 75% 60%, var(--navy-mid) 0%, transparent 60%),
      linear-gradient(180deg, var(--navy) 0%, var(--navy-deep) 100%);
  }
  .card-band {
    position: absolute;
    left: 0;
    right: 0;
    bottom: 0;
    background: var(--band);
    border-top: 1px solid var(--rule);
  }

  /* Front */
  .card-front {
    left: 43px;
    top: 31px;
    width: 623px;
    height: 369px;
  }
  .card-front .card-band { height: 34px; }
  .front-mark {
    position: absolute;
    left: 50%;
    top: 58px;
    transform: translateX(-50%);
  }
  .front-name {
    position: absolute;
    left: 0;
    right: 0;
    top: 206px;
    text-align: center;
    font-family: "Open Sans", Arial, sans-serif;
    font-weight: 400;
    font-size: 54px;
    line-height: 1.2;
    color: var(--text-light);
  }

  /* Back */
  .card-back {
    left: 516px;
    top: 396px;
    width: 618px;
    height: 352px;
  }
  .card-back .card-band { height: 44px; }
  .back-mark {
    position: absolute;
    left: 60px;
    top: 50px;
  }
  .info-panel {
    position: absolute;
    left: 313px;
    top: 0;
    right: 0;
    bottom: 44px;
    background: var(--panel);
    border-left: 1px solid var(--rule);
  }
  .holder {
    position: absolute;
    left: 60px;
    width: 250px;
    top: 152px;
    text-align: center;
    color: var(--text-light);
  }
  .holder-name {
    font-family: "Tinos", "Times New Roman", serif;
    font-weight: 700;
    font-size: 30px;
    line-height: 1.1;
  }
  .holder-title {
    font-family: "Open Sans", Arial, sans-serif;
    font-size: 17px;
    color: var(--text-soft);
  }
  .contact {
    position: absolute;
    right: 42px;
    top: 76px;
    text-align: right;
    font-family: "Open Sans", Arial, sans-serif;
    color: var(--text-light);
  }
  .contact-company {
    font-size: 28px;
    font-weight: 400;
    margin-bottom: 22px;
  }
  .contact-line {
    font-size: 16px;
    line-height: 21px;
  }
  .contact-gap { margin-top: 8px; }
  .web {
    position: absolute;
    left: 0;
    right: 0;
    bottom: 13px;
    text-align: center;
    font-family: "Open Sans", Arial, sans-serif;
    font-size: 16px;
    color: var(--text-light);
  }
</style>
</head>
<body>
<main class="canvas">

  <section class="card card-front" aria-label="Card front">
    <div class="card-bokeh" role="img" aria-label="Deep blue background with soft blurred light spots"></div>
    <svg class="front-mark" width="120" height="120" viewBox="0 0 120 120" aria-hidden="true">
      <circle cx="60" cy="60" r="55" fill="none" stroke="var(--mark-line)" stroke-width="5"/>
    </svg>
    <div class="front-name">quorvaAgency</div>
    <div class="card-band"></div>
  </section>

  <section class="card card-back" aria-label="Card back">
    <div class="card-bokeh" role="img" aria-label="Deep blue background with soft blurred light spots"></div>
    <svg class="back-mark" width="250" height="250" viewBox="0 0 250 250" aria-hidden="true">
      <circle cx="125" cy="125" r="118" fill="none" stroke="rgba(140,180,235,0.25)" stroke-width="8"/>
    </svg>
    <div class="info-panel"></div>
    <div class="holder">
      <div class="holder-name">Your Name</div>
      <div class="holder-title">Job Title</div>
    </div>
    <div class="contact">
      <div class="contact-company">quorvaAgency</div>
      <div class="contact-line">yourname@yourcompany.com</div>
      <div class="contact-line">232 address Lane1,</div>
      <div class="contact-line">Address Lane 2,</div>
      <div class="contact-line contact-gap">Mobile Number</div>
      <div class="contact-line">Phone Number</div>
      <div class="contact-line">Fax Number</div>
    </div>
    <div class="card-band"></div>
    <div class="web">www.yourcompany.com</div>
  </section>

</main>
</body>
</html>
```